uLark

We need ideas for powerpoint template. Please submit several designs from simple/basic to elaborate/detailed using our company's logo. Please match designs with our logo color. We're very open to ideas. "Harbors Harmonized" can be removed

```html
<!DOCTYPE html>
<html lang="en">
<head>
<meta charset="utf-8">
<title>uLark – presentation template set</title>
<link rel="stylesheet" href="https://fonts.googleapis.com/css2?family=Lato:wght@400;700&family=Montserrat:wght@500;600;700&display=swap">
<style>
  :root {
    --stage: #000000;
    --paper: #ffffff;
    --teal-deep: #2f7389;
    --teal-mid: #3f8f99;
    --teal-light: #5aaba8;
    --teal-title: #5bb5b0;
    --teal-accent: #26a597;
    --brand-ink: #2f7f8c;
    --panel: #f4f5f5;
    --photo: #b9bcbd;
    --body-ink: #8a8d8e;
    --name-ink: #555a5b;
  }
  * { box-sizing: border-box; margin: 0; padding: 0; }
  html, body { width: 1200px; height: 883px; overflow: hidden; background: var(--stage); }
  .board { position: relative; width: 1200px; height: 883px; }

  .slide {
    position: absolute; width: 557px; height: 395px; overflow: hidden;
    background: var(--paper); font-family: "Lato", sans-serif;
  }
  .slide--cover-dark { left: 27px; top: 30px;
    background: radial-gradient(ellipse 60% 70% at 68% 32%, var(--teal-light) 0%, var(--teal-mid) 45%, var(--teal-deep) 100%); }
  .slide--cover-light { left: 616px; top: 30px; }
  .slide--stats { left: 27px; top: 457px; }
  .slide--team { left: 616px; top: 457px; }

  .slide-title {
    position: absolute; font-family: "Montserrat", sans-serif; font-weight: 600;
    color: var(--teal-title); letter-spacing: 0.5px; white-space: nowrap;
  }
  .slide--cover-dark .slide-title { left: 49px; top: 33px; font-size: 29px; color: var(--paper); }
  .slide--cover-light .slide-title { left: 44px; top: 25px; font-size: 31px; }
  .slide--stats .slide-title { left: 29px; top: 25px; font-size: 24px; }
  .slide--team .slide-title { left: 16px; top: 20px; font-size: 24px; }

  /* brand lockup */
  .brand { position: absolute; text-align: center; transform: translateX(-50%); }
  .brand-dot { border-radius: 50%; margin: 0 auto; }
  .brand-name { font-family: "Lato", sans-serif; font-weight: 400; line-height: 1; }
  .brand-tag { font-family: "Lato", sans-serif; font-weight: 400; line-height: 1; white-space: nowrap; }

  .brand--large { top: 113px; left: 277px; }
  .brand--large .brand-dot { width: 116px; height: 116px; }
  .brand--large .brand-name { font-size: 28px; margin-top: 6px; }
  .brand--large .brand-tag { font-size: 13.5px; margin-top: 5px; }
  .slide--cover-dark .brand-dot { background: var(--paper); }
  .slide--cover-dark .brand-name, .slide--cover-dark .brand-tag { color: var(--paper); }
  .slide--cover-light .brand { top: 121px; }
  .slide--cover-light .brand-dot { background: var(--teal-mid); }
  .slide--cover-light .brand-name, .slide--cover-light .brand-tag { color: var(--brand-ink); }

  .brand--small { top: 10px; left: 497px; }
  .brand--small .brand-dot { width: 48px; height: 48px; background: var(--teal-mid); }
  .brand--small .brand-name { font-size: 10px; margin-top: 4px; color: var(--brand-ink); }
  .brand--small .brand-tag { font-size: 5px; margin-top: 2px; color: var(--brand-ink); }

  .content-panel { position: absolute; background: var(--panel); }
  .slide--stats .content-panel { left: 19px; top: 107px; width: 523px; height: 272px; }
  .slide--team .content-panel { left: 19px; top: 102px; width: 518px; height: 253px; }

  /* stats */
  .stat { position: absolute; top: 0; width: 170px; transform: translateX(-50%); text-align: center; }
  .stat-ring { position: absolute; left: 17px; top: 20px; }
  .stat-value {
    position: absolute; left: 0; right: 0; top: 71px;
    font-family: "Montserrat", sans-serif; font-weight: 700; font-size: 26px; color: var(--teal-accent);
  }
  .stat-label {
    position: absolute; left: 0; right: 0; top: 180px;
    font-family: "Montserrat", sans-serif; font-weight: 600; font-size: 18px; color: var(--teal-accent);
  }
  .stat-text {
    position: absolute; left: 20px; right: 20px; top: 206px;
    font-size: 9px; line-height: 14px; color: var(--body-ink);
  }

  /* team */
  .member { position: absolute; top: 0; width: 170px; transform: translateX(-50%); text-align: center; }
  .member-photo {
    width: 86px; height: 86px; margin: 5px auto 0; border-radius: 50%;
    background: radial-gradient(circle at 50% 40%, #d6d8d9 0%, var(--photo) 70%);
    border: 2px solid var(--paper);
  }
  .member-name {
    margin-top: 9px; font-family: "Lato", sans-serif; font-weight: 400; font-size: 14.5px;
    color: var(--teal-accent); letter-spacing: 0.2px; white-space: nowrap;
  }
  .member-company { margin-top: 2px; font-size: 9px; color: var(--name-ink); }
  .member-bio { margin: 3px 12px 0; font-size: 8.4px; line-height: 13.6px; color: var(--body-ink); }
</style>
</head>
<body>
<main class="board">

  <section class="slide slide--cover-dark">
    <h1 class="slide-title">Title here</h1>
    <div class="brand brand--large">
      <div class="brand-dot"></div>
      <p class="brand-name">uLark</p>
      <p class="brand-tag">Harbors Harmonized</p>
    </div>
  </section>

  <section class="slide slide--cover-light">
    <h1 class="slide-title">Title here</h1>
    <div class="brand brand--large">
      <div class="brand-dot"></div>
      <p class="brand-name">uLark</p>
      <p class="brand-tag">Harbors Harmonized</p>
    </div>
  </section>

  <section class="slide slide--stats">
    <h2 class="slide-title">Title here</h2>
    <div class="brand brand--small">
      <div class="brand-dot"></div>
      <p class="brand-name">uLark</p>
      <p class="brand-tag">Harbors Harmonized</p>
    </div>
    <div class="content-panel">
      <div class="stat" style="left:88px">
        <svg class="stat-ring" width="136" height="136" viewBox="0 0 136 136">
          <circle cx="68" cy="68" r="67" fill="none" stroke="var(--teal-accent)" stroke-width="2.5"
            stroke-dasharray="368 421" transform="rotate(130 68 68)"/>
        </svg>
        <p class="stat-value">88%</p>
        <p class="stat-label">ADD TEXT</p>
        <p class="stat-text">Lorem ipsum dolore sit amet, et, tristique urna lorem sed morbi leo curabitur vitae et, dicta sunt</p>
      </div>
      <div class="stat" style="left:260px">
        <svg class="stat-ring" width="136" height="136" viewBox="0 0 136 136">
          <circle cx="68" cy="68" r="67" fill="none" stroke="var(--teal-accent)" stroke-width="2.5"
            stroke-dasharray="330 421" transform="rotate(180 68 68)"/>
        </svg>
        <p class="stat-value">88%</p>
        <p class="stat-label">ADD TEXT</p>
        <p class="stat-text">Lorem ipsum dolore sit amet, et, tristique urna lorem sed morbi leo curabitur vitae et, dicta sunt</p>
      </div>
      <div class="stat" style="left:434px">
        <svg class="stat-ring" width="136" height="136" viewBox="0 0 136 136">
          <circle cx="68" cy="68" r="67" fill="none" stroke="var(--teal-accent)" stroke-width="2.5"
            stroke-dasharray="250 421" transform="rotate(-115 68 68)"/>
        </svg>
        <p class="stat-value">88%</p>
        <p class="stat-label">ADD TEXT</p>
        <p class="stat-text">Lorem ipsum dolore sit amet, et, tristique urna lorem sed morbi leo curabitur vitae et, dicta sunt</p>
      </div>
    </div>
  </section>

  <section class="slide slide--team">
    <h2 class="slide-title">Title here</h2>
    <div class="brand brand--small">
      <div class="brand-dot"></div>
      <p class="brand-name">uLark</p>
      <p class="brand-tag">Harbors Harmonized</p>
    </div>
    <div class="content-panel">
      <div class="member" style="left:81px">
        <div class="member-photo" role="img" aria-label="Portrait photo of a team member"></div>
        <p class="member-name">EMPLOYEE NAME</p>
        <p class="member-company">Company Name</p>
        <p class="member-bio">Liquorice sugar drops applicake apple pie cupcake brownie bear claw cake gingerbread cotton candy. Bear claw croissant apple pie. Croissant cake sweet puff wafer . Liquorice sugar drops applicake apple pie cupcake brownie bear claw cake gingerbread cotton candy.</p>
      </div>
      <div class="member" style="left:252px">
        <div class="member-photo" role="img" aria-label="Portrait photo of a team member"></div>
        <p class="member-name">EMPLOYEE NAME</p>
        <p class="member-company">Company Name</p>
        <p class="member-bio">Liquorice sugar drops applicake apple pie cupcake brownie bear claw cake gingerbread cotton candy. Bear claw croissant apple pie. Croissant cake sweet puff wafer . Liquorice sugar drops applicake apple pie cupcake brownie bear claw cake gingerbread cotton candy.</p>
      </div>
      <div class="member" style="left:431px">
        <div class="member-photo" role="img" aria-label="Portrait photo of a team member"></div>
        <p class="member-name">EMPLOYEE NAME</p>
        <p class="member-company">Company Name</p>
        <p class="member-bio">Liquorice sugar drops applicake apple pie cupcake brownie bear claw cake gingerbread cotton candy. Bear claw croissant apple pie. Croissant cake sweet puff wafer . Liquorice sugar drops applicake apple pie cupcake brownie bear claw cake gingerbread cotton candy.</p>
      </div>
    </div>
  </section>

</main>
</body>
</html>
```